Sudden Tides "Lantern Road" New Single Cover

Create cover artwork for the band Sudden Tides' new single "Lantern Road" being released early 2020. Style, font and graphics to be consistent with band's previous releases and overall brand identity. Visit www.suddentidesband.example and our Spotify page https://music.example.net/artist/7QzWpLx3RtVnKd8e2YbHcJ?si=MUrTgKa4PLe7skvWq2AmZd to view our previous releases and overall brand identity. Some examples attached as well. We are looking for someone to work with on future projects as well.

Lyrics are here: https://docs.example.org/document/d/3KTp9wrn_2ZQa8eXb4Lo_fimH7C5m83Jz4Pd70hrtVcA/edit

Music is here: https://audiostream.example.com/suddentides/lantern-road/s-pzkwa

Font styles to use
Sans Serif

Colors

Designer to choose colors to be used in the design.

Requirements
Must have
• Must be consistent with current brand identity and with prior album / single art.

```html
<!DOCTYPE html>
<html lang="en">
<head>
<meta charset="utf-8">
<title>Sudden Tides – Lantern Road</title>
<link rel="stylesheet" href="https://fonts.googleapis.com/css2?family=Josefin+Sans:wght@300;400&display=swap">
<style>
  :root {
    --backdrop: #000000;
    --cover-yellow: #EBB02D;
    --title-white: #FFFFFF;
    --band-navy: #1E2A5E;
  }
  html, body {
    margin: 0;
    padding: 0;
    width: 1200px;
    height: 1200px;
    overflow: hidden;
    background: var(--backdrop);
  }
  .cover {
    position: absolute;
    left: 221px;
    top: 205px;
    width: 790px;
    height: 790px;
    background: var(--cover-yellow);
    font-family: "Josefin Sans", sans-serif;
  }
  .single-title {
    position: absolute;
    left: 0;
    right: 0;
    margin: 0;
    text-align: center;
    color: var(--title-white);
    font-weight: 300;
    font-size: 122px;
    line-height: 1;
    letter-spacing: 0.14em;
    text-indent: 0.14em;
  }
  .single-title--first { top: 160px; }
  .single-title--second { top: 375px; }
  .band-name {
    position: absolute;
    left: 0;
    right: 0;
    top: 620px;
    margin: 0;
    text-align: center;
    color: var(--band-navy);
    font-weight: 400;
    font-size: 32px;
    line-height: 1.15;
    letter-spacing: 0.12em;
    text-indent: 0.12em;
  }
</style>
</head>
<body>
  <main class="cover">
    <h1 class="single-title single-title--first">LANTERN</h1>
    <p class="single-title single-title--second">ROAD</p>
    <p class="band-name">SUDDEN<br>TIDES</p>
  </main>
</body>
</html>
```